Redesign of Plastic Surgeon Website to fully responsive / modern feel

Hi

Our current website is out of date www.harbourlinecosmetic.org

We want a fresh / modern looking design
Needs to be fully responsive design that works extremely well on ipad and mobile device

Would like design for both full screen website and mobile

Have listed a few websites of other plastic surgeons we like
http://www.reformclinicdaily.com/
http://www.peterholtbymd.com/
http://www.corvanbeauty.com/
http://www.tidewellcontouring.com/

Menu needs to include
1. About Us
2. Procedures (see current website for example)
3. News
4. Patient Resources
5. Contact Us

We are flexible with colours / images / layout

I have uploaded a document that has some content - the face pages content is completed only

some of the procedures can have content upwards of 4000 words - total website can be large with over 40,000 words
Updates

Target Market(s)

Mainly women 20-60 85% of practice
Some men 15%

Industry/Entity Type

Plastic Surgery

Number of Pages Required

5+ page

Requirements
Must have
• We need designs for
• Homepage
• Internal pages
• 1. Landing pages for breast / body / face / non surgical main pages
• 2. Procedure pages for individual pages under each section - eg breast augmentation
• 3. About us pages - like meet the doctor, our staff, clinics
• 4. Contact page
• 5. Blog / News page
Nice to have
• See our list of websites for examples of designs we like
• Like full screen design with nice hero image
• Needs to have good to call to action messages on home page like
• Specials, procedure of the month, etc

```html
<!DOCTYPE html>
<html lang="en">
<head>
<meta charset="utf-8">
<title>Harbourline Institute of Plastic Surgery</title>
<link href="https://fonts.googleapis.com/css2?family=Roboto+Condensed:wght@300;400;700&family=Roboto:wght@300;400;500&display=swap" rel="stylesheet">
<style>
:root{
  --orange:#e0a063;
  --orange-deep:#e4801d;
  --orange-text:#c9762a;
  --ink:#333;
  --muted:#555;
  --paper:#fff;
  --mist:#f0f0f0;
  --band:#3a3a3a;
  --foot:#2d2d2d;
  --foot-text:#bdbdbd;
}
*{margin:0;padding:0;box-sizing:border-box}
html,body{width:778px;height:1200px;overflow:hidden;background:var(--paper)}
body{position:relative;font-family:"Roboto",sans-serif;color:var(--ink)}
.abs{position:absolute}
.header{left:0;top:0;width:778px;height:60px;background:var(--paper)}
.brand{left:152px;top:12px;display:flex;align-items:center;gap:6px;font-family:"Roboto Condensed",sans-serif;font-size:15px;color:var(--orange-text);line-height:1.05;font-weight:400}
.brand-dot{width:14px;height:14px;border-radius:50%;background:var(--orange)}
.search{left:338px;top:22px;width:162px;height:20px;border:1px solid #bbb;font-size:9px;color:#aaa;padding:4px 6px}
.search svg{position:absolute;right:4px;top:3px}
.phone{left:528px;top:12px;text-align:left;font-family:"Roboto Condensed",sans-serif;color:#444}
.phone b{display:block;font-weight:400;font-size:19px;letter-spacing:.5px}
.phone span{font-size:10px}
.nav{left:0;top:60px;width:778px;height:30px;background:var(--orange);display:flex;justify-content:center;align-items:center}
.nav a{color:#fff;font-size:9px;text-decoration:none;padding:0 9px;border-right:1px solid rgba(255,255,255,.4)}
.nav a:last-child{border-right:none}
.hero{left:0;top:90px;width:778px;height:255px;background:linear-gradient(90deg,#111 0%,#2a2a2a 45%,#6a6a6a 100%)}
.hero-photo{left:430px;top:0;width:348px;height:255px;background:radial-gradient(ellipse at 55% 45%,#e8c8b0 0%,#b89078 40%,rgba(80,80,80,0) 75%)}
.hero-text{left:152px;top:44px;color:#fff;font-family:"Roboto Condensed",sans-serif;font-weight:300}
.hero-text .l1{font-size:27px}
.hero-text .l2{font-size:32px;font-weight:400;margin-top:2px}
.hero-text .l3{font-size:24px;margin-top:2px}
.btn{left:152px;top:255px;width:90px;height:27px;background:var(--orange-deep);color:#fff;font-size:12px;display:flex;align-items:center;justify-content:center;border-radius:2px}
.tile{top:345px;height:148px;overflow:hidden}
.tile-photo{position:absolute;left:0;top:0;width:100%;height:110px}
.tile-label{position:absolute;left:0;bottom:0;width:100%;height:38px;display:flex;align-items:center;justify-content:center;color:#fff;font-family:"Roboto Condensed",sans-serif;font-size:14px}
.t1{left:0;width:258px;background:#111}
.t1 .tile-photo{background:linear-gradient(90deg,#c9a88e,#e0c6b2 50%,#c9a88e)}
.t2{left:258px;width:262px;background:var(--orange)}
.t2 .tile-photo{background:linear-gradient(180deg,#fff,#f3e4d8)}
.t3{left:520px;width:258px;background:linear-gradient(90deg,#6d6d6d,#a79388 55%,#d9c0ad)}
.t3 .specials{position:absolute;left:10px;top:68px;color:#fff;font-family:"Roboto Condensed",sans-serif;font-size:19px}
.philosophy{left:0;top:493px;width:778px;height:252px;background:var(--mist)}
.section-title{font-family:"Roboto Condensed",sans-serif;font-weight:400;color:var(--orange-text);text-align:center}
.philosophy .section-title{position:absolute;left:0;width:778px;top:17px;font-size:21px}
.col h3{font-family:"Roboto Condensed",sans-serif;font-weight:400;font-size:16px;text-align:center;color:#222;margin-bottom:6px}
.col p{font-size:6.8px;line-height:1.4;text-align:center;color:var(--muted);margin-bottom:7px}
.vision{left:152px;top:57px;width:148px}
.vision .mission-title{margin-top:18px}
.values{left:318px;top:57px;width:276px}
.meet{left:0;top:745px;width:778px;height:200px;background:linear-gradient(135deg,#fff,#f4f4f4)}
.divider{left:333px;top:15px;width:1px;height:170px;background:#aaa}
.meet .section-title{position:absolute;font-size:21px}
.doc-title{left:150px;top:10px;width:182px}
.staff-title{left:350px;top:10px;width:270px}
.portrait{background:linear-gradient(180deg,#8a7a70,#c6a894 60%,#3a3a3a)}
.doc-photo{left:204px;top:43px;width:60px;height:68px}
.doc-text{left:154px;top:119px;width:164px;font-size:6.6px;line-height:1.4;text-align:center;color:var(--muted)}
.staff-text{left:350px;top:40px;width:270px;font-size:6.6px;line-height:1.4;text-align:center;color:var(--muted)}
.more{color:#b23;font-size:6.6px;display:block;text-align:center;margin-top:1px}
.staff{top:113px;width:48px;text-align:center}
.staff .portrait{height:60px;width:48px}
.staff span{display:block;font-size:6.5px;color:#444;margin-top:4px;white-space:nowrap;margin-left:-8px;width:64px}
.badges{left:0;top:945px;width:778px;height:68px;background:var(--band);display:flex;justify-content:center;align-items:center;gap:36px}
.badge{width:38px;height:24px;border:1px solid #999;border-radius:50%}
.badge.sq{border-radius:2px;width:46px}
.footer{left:0;top:1013px;width:778px;height:187px;background:var(--foot);color:var(--foot-text)}
.fcol{top:13px;font-size:7px;line-height:1.65}
.fcol h4{color:#fff;font-size:8px;font-weight:500;margin-bottom:3px}
.fcol b{color:#fff;font-weight:500}
.form{left:510px;top:13px;width:116px}
.form h4{color:#fff;font-size:8px;font-weight:500;margin-bottom:4px}
.field{background:#fff;height:13px;margin-bottom:3px;font-size:6px;color:#999;padding:2px 4px}
.field.msg{height:30px}
.send{width:38px;height:13px;background:var(--orange);color:#fff;font-size:6.5px;display:flex;align-items:center;justify-content:center;margin-top:4px}
.frule{left:140px;top:153px;width:498px;height:1px;background:#555}
.flinks{left:0;top:162px;width:778px;text-align:center;font-size:6.6px;color:var(--foot-text)}
.copy{left:0;top:176px;width:778px;text-align:center;font-size:6px;color:#999}
</style>
</head>
<body>
<header class="abs header">
  <div class="abs brand"><span class="brand-dot"></span><span>Harbourline Institute<br>of Plastic Surgery</span></div>
  <div class="abs search">Search
    <svg width="12" height="12" viewBox="0 0 12 12"><circle cx="5" cy="5" r="3.6" fill="none" stroke="#888" stroke-width="1.2"/><path d="M7.6 7.6 11 11" stroke="#888" stroke-width="1.4"/></svg>
  </div>
  <div class="abs phone"><b>02 5550 1750</b><span>CALL FOR APPOINTMENTS ?</span></div>
</header>
<nav class="abs nav"><a>Home</a><a>About Us</a><a>Procedures</a><a>News</a><a>Patient Resources</a><a>Contact Us</a></nav>

<section class="abs hero">
  <div class="abs hero-photo" role="img" aria-label="Portrait photo of a woman with smooth skin"></div>
  <div class="abs hero-text">
    <div class="l1">At the Institute of</div>
    <div class="l2">Aesthetic Plastic Surgery</div>
    <div class="l3">Your future looks beautiful</div>
  </div>
</section>
<div class="abs btn">Read More</div>

<div class="abs tile t1">
  <div class="tile-photo" role="img" aria-label="Before and after photos of a back after body contouring"></div>
  <div class="tile-label">Procedure of the Month</div>
</div>
<div class="abs tile t2">
  <div class="tile-photo" role="img" aria-label="Photo of a woman measuring her waist before and after"></div>
  <div class="tile-label">Body Contouring / Fat Reduction</div>
</div>
<div class="abs tile t3" role="img" aria-label="Photo of a patient marked for facial surgery">
  <div class="specials">Specials</div>
</div>

<section class="abs philosophy">
  <h2 class="section-title">Our Philosophy and Values</h2>
  <div class="abs col vision">
    <h3>Our Vision</h3>
    <p>With advanced techniques, expertise and constant client feedback, we aim to remain at the forefront of surgical rejuvenation and deliver outstanding results for clients who value experience, empathy and quality outcomes.</p>
    <h3 class="mission-title">Our Mission</h3>
    <p>To provide exceptional quality of service in plastic and cosmetic surgery, and improve the appearance, wellbeing and self confidence of clients entrusting us with their care.</p>
  </div>
  <div class="abs col values">
    <h3>Our Values</h3>
    <p>» Integrity – We aim to impress with education rather than promotion. All photographs on this website are of Dr Halvorsen's own clients, and are not enhanced or digitally embellished. The outcomes of surgery shown are true representations of our results.</p>
    <p>» Accessibility – Peace of mind with 24/7 service. All clients have direct access to Dr Halvorsen and his team before, during and after surgical procedures.</p>
    <p>» Empathy – We treat clients with absolute respect. You can feel confident sharing your choices, opinions and feelings with our sincere, mature and non-judgemental staff.</p>
    <p>» Privacy – Absolute discretion. Your details and treatment history are kept in strict confidence at all times.</p>
    <p>» Feedback – Your thoughts and feelings are important to us. We encourage feedback, comments and suggestions to ensure satisfaction with every aspect of your experience.</p>
    <p>» Progress – Ongoing professional development ensures all our staff members remain up to date with the latest techniques and operations.</p>
  </div>
</section>

<section class="abs meet">
  <div class="abs divider"></div>
  <h2 class="section-title doc-title">Meet Dr Halvorsen</h2>
  <div class="abs portrait doc-photo" role="img" aria-label="Portrait photo of the surgeon"></div>
  <div class="abs doc-text">Dr Halvorsen's goal has remained the same from the day he elected to become a surgeon: to provide his patients with natural, beautiful results. Today, his thriving practice is testament to what he set out to achieve from the very beginning: changing a person's quality of life, through self-improvement.<span class="more">Read More</span></div>
  <h2 class="section-title staff-title">Meet Our Staff</h2>
  <div class="abs staff-text">Our nursing and patient support teams sole goal is to support our patients who trust us with their care. You can feel confident of their support and expertise at every step of your transformative journey. We treat every patient with absolute respect, so you can be comfortable in our sincere, friendly and supportive environment. A keynote of our service is the availability of Dr Halvorsen and his staff on a 24/7 basis. This service is unique and is informed by our own personal experiences of being patients and family in the strange world of being unwell.<span class="more">Read More</span></div>
  <div class="abs staff" style="left:350px"><div class="portrait" role="img" aria-label="Staff portrait photo"></div><span>Mia Carrow</span></div>
  <div class="abs staff" style="left:418px"><div class="portrait" role="img" aria-label="Staff portrait photo"></div><span>Tess Whitlow</span></div>
  <div class="abs staff" style="left:491px"><div class="portrait" role="img" aria-label="Staff portrait photo"></div><span>Ruth Ansley</span></div>
  <div class="abs staff" style="left:559px"><div class="portrait" role="img" aria-label="Staff portrait photo"></div><span>Dana Pell</span></div>
</section>

<div class="abs badges" aria-label="Professional memberships">
  <div class="badge"></div><div class="badge"></div><div class="badge"></div><div class="badge sq"></div><div class="badge sq"></div><div class="badge sq"></div><div class="badge sq"></div>
</div>

<footer class="abs footer">
  <div class="abs fcol" style="left:152px"><h4>Face</h4>» Facelift<br>» Eyelid Surgery<br>» Brow Lift Surgery<br>» Rhinoplasty Surgery<br>» Otoplasty Surgery<br>» Laser Resurfacing</div>
  <div class="abs fcol" style="left:234px"><h4>Body</h4>» Tummy Tuck<br>» Liposuction Brachioplasty<br>» Chin Enlargement</div>
  <div class="abs fcol" style="left:328px"><h4>Breast</h4>» Breast Augmentation<br>» Breast Reduction<br>» Breast Lift<br>» Breast Reconstruction<br>» Gynecomastia</div>
  <div class="abs fcol" style="left:410px;line-height:1.35"><h4>Our Clinics</h4><b>Northbay</b><br>412 Seawall Rd, Suite 12<br>Northbay, NSW 2999<br><br><b>Elmwood</b><br>Level 1<br>77 Linden Street<br>2998<br>Tel: 02 5550 1750</div>
  <div class="abs form"><h4>Book Your Free Consultation</h4>
    <div class="field">Yours Name</div><div class="field">Yours Number</div><div class="field">Email</div><div class="field">Subject</div><div class="field msg">Message</div>
    <div class="send">Send</div>
  </div>
  <div class="abs frule"></div>
  <div class="abs flinks">Home | Disclaimer | Privacy | Sitemap | Feedback | Tell a friend | Contact Us | Find us online</div>
  <div class="abs copy">© Harbourline Institute of Plastic Surgery Dr Erik Halvorsen Plastic Surgery Harbourline</div>
</footer>
</body>
</html>
```